2017 New Year Membership Sale

I require a flyer to be designed for a mail box drop.

We are a 24/7 Gym and will be running a sale in January. No Joining Fee, Flexible membership options.

We are also going to have an open day on Saturday the 21st of January, everyone is welcome. Supplement samples and information. Free health measurements. Free starter PT pack if you join on the day.

We offer a 24/7 DIY gym as well as a comprehensive Personal Training Studio.

I have included the design I used last year.

Target Market(s)

Potential Members of all ages.

Industry/Entity Type

Gym

Requirements
Must have
• Our Address, Phone Number.
• Staffed Hours;
• Mon-Thur: 12pm - 7pm
• Fri-Sat: 8am - 1pm

```html
<!DOCTYPE html>
<html lang="en">
<head>
<meta charset="utf-8">
<title>January Membership Sale Flyer</title>
<link href="https://fonts.googleapis.com/css2?family=Oswald:wght@700&family=Exo+2:wght@500;600;700&display=swap" rel="stylesheet">
<style>
  :root {
    --page: #e9e9e7;
    --ink: #15171b;
    --panel: #1a1c21;
    --teal: #2c8e9e;
    --teal-deep: #1d4d57;
    --orange: #f0821e;
    --white: #ffffff;
    --grey: #b9c0c6;
  }
  * { margin: 0; padding: 0; box-sizing: border-box; }
  html, body { width: 1200px; height: 900px; overflow: hidden; background: var(--page); }
  .flyer {
    position: absolute; left: 296px; top: 20px; width: 608px; height: 860px;
    background: var(--panel); overflow: hidden;
    font-family: "Exo 2", sans-serif; color: var(--white);
    box-shadow: 0 6px 18px rgba(0,0,0,.25);
  }
  .flyer-shapes { position: absolute; inset: 0; }
  .headline {
    position: absolute; left: 10px; top: 110px; width: 300px;
    transform: rotate(-52deg); transform-origin: center;
    font-family: "Oswald", sans-serif; font-size: 52px; line-height: 0.95;
    text-transform: uppercase; letter-spacing: 1px;
  }
  .headline .accent { color: var(--orange); }
  .open-hours-badge {
    position: absolute; left: 62px; top: 325px;
    font-family: "Exo 2", sans-serif; font-weight: 700; font-size: 32px; line-height: 0.95;
    color: #dfe6ea;
  }
  .welcome { position: absolute; left: 345px; top: 420px; }
  .welcome-title {
    font-weight: 700; font-size: 34px; line-height: 0.92; color: var(--teal);
    text-transform: uppercase; letter-spacing: 1px;
  }
  .perks { list-style: none; margin-top: 14px; }
  .perks li {
    position: relative; padding-left: 18px; margin-bottom: 9px;
    font-weight: 600; font-size: 14px; line-height: 1.15; text-transform: uppercase; letter-spacing: .3px;
  }
  .perks li::before {
    content: ""; position: absolute; left: 2px; top: 4px; width: 9px; height: 9px;
    border-radius: 50%; background: var(--teal);
  }
  .hours { position: absolute; left: 353px; top: 676px; }
  .hours-title { font-weight: 700; font-size: 18px; color: var(--teal); text-transform: uppercase; letter-spacing: .5px; }
  .hours p { font-weight: 600; font-size: 15px; line-height: 1.35; }
  .call { position: absolute; left: 348px; top: 770px; }
  .call-label { font-weight: 700; font-size: 24px; line-height: 1; color: var(--orange); text-transform: uppercase; }
  .call-number { font-weight: 700; font-size: 46px; line-height: 1; color: var(--orange); letter-spacing: 1px; }
  .open-day {
    position: absolute; left: 167px; top: 587px; width: 156px; height: 156px;
    display: flex; flex-direction: column; align-items: center; justify-content: center; text-align: center;
    text-transform: uppercase; color: var(--orange); font-weight: 700;
  }
  .open-day-title { font-size: 20px; line-height: 1; }
  .open-day-date { font-size: 14px; line-height: 1.2; }
  .brand { position: absolute; left: 14px; top: 768px; display: flex; align-items: center; gap: 8px; }
  .brand-dot { width: 16px; height: 16px; border-radius: 50%; background: var(--white); }
  .brand-name { font-weight: 700; font-size: 24px; color: var(--white); }
  .brand-location {
    position: absolute; left: 12px; top: 820px;
    font-weight: 500; font-size: 16px; letter-spacing: 8px; color: var(--white);
  }
</style>
</head>
<body>
<main class="flyer">
  <svg class="flyer-shapes" width="608" height="860" viewBox="0 0 608 860" aria-hidden="false">
    <defs>
      <linearGradient id="heroGrad" x1="0" y1="0" x2="1" y2="1">
        <stop offset="0" stop-color="#2a3a44"/>
        <stop offset="0.6" stop-color="#1f4c56"/>
        <stop offset="1" stop-color="#2a2e33"/>
      </linearGradient>
      <linearGradient id="studioGrad" x1="0" y1="0" x2="1" y2="1">
        <stop offset="0" stop-color="#dfe5ea"/>
        <stop offset="1" stop-color="#8d99a4"/>
      </linearGradient>
    </defs>
    <rect class="hero-photo" x="0" y="0" width="608" height="385" fill="url(#heroGrad)" role="img" aria-label="Photo of an athlete training with a dumbbell in the gym"/>
    <polygon points="190,385 0,385 0,360 350,0 400,0" fill="#1e5863" opacity="0.75"/>
    <polygon points="0,0 352,0 0,362" fill="#17191d"/>
    <rect class="studio-photo" x="0" y="385" width="350" height="162" fill="url(#studioGrad)" role="img" aria-label="Photo of treadmills and cardio machines in the gym"/>
    <rect class="area-map" x="0" y="547" width="350" height="210" fill="#ecebe6" role="img" aria-label="Street map showing the gym location"/>
    <g class="map-pin" transform="translate(65,612)">
      <path d="M0 0c-5 0-8 4-8 8 0 6 8 14 8 14s8-8 8-14c0-4-3-8-8-8z" fill="#d9362b"/>
      <circle cx="0" cy="8" r="3" fill="#fff"/>
    </g>
    <polygon points="345,385 380,385 125,680 90,680" fill="var(--orange)"/>
    <polygon points="0,860 305,860 130,665 0,770" fill="var(--orange)"/>
    <circle cx="245" cy="665" r="78" fill="#25272b" stroke="#d9d9d9" stroke-width="2"/>
  </svg>

  <h1 class="headline">Huge <span class="accent">Sale</span><br>In <span class="accent">January</span></h1>
  <p class="open-hours-badge">24/7<br>OPEN</p>

  <section class="welcome">
    <h2 class="welcome-title">Everyone<br>is welcome</h2>
    <ul class="perks">
      <li>No joining fee</li>
      <li>Flexible<br>membership options</li>
      <li>Supplement samples<br>and information</li>
      <li>Free measurements</li>
      <li>Free starter PT pack</li>
    </ul>
  </section>

  <section class="open-day">
    <p class="open-day-title">Open Day</p>
    <p class="open-day-date">On Saturday 21<sup>st</sup><br>January</p>
  </section>

  <section class="hours">
    <h3 class="hours-title">Staffed Hours</h3>
    <p>Monday-Thursday: 12pm - 7pm</p>
    <p>Friday-Saturday: 8am - 1pm</p>
  </section>

  <section class="call">
    <p class="call-label">Call us now</p>
    <p class="call-number">35550142</p>
  </section>

  <div class="brand">
    <span class="brand-dot"></span>
    <span class="brand-name">Pulsewave Fitness</span>
  </div>
  <p class="brand-location">HOLLOWMERE</p>
</main>
</body>
</html>
```